RVT Business Card Design

We are an independent auto dealer who specializes in commercial & fleet vehicles, we are family owned and operated and have been in business since 2001. We stock late model, low mileage, white trucks & vans. We mostly deal with companies in the construction and service industries. We are just looking to try to freshen up our old business card, we do not want to change the logo at this point, because it is well know within the southwest region & construction community. I have attached our logo and a PDF of our current business card for reference.
Updates
If the address is stacked there is no comma (,) after NE. Everyone keeps putting it in with this format and it is not correct.
482 Montrose Ave NE
Albuquerque, NM 87193
If the address is all on one line, then there will be a comma (,) after NE
482 Montrose Ave NE, Albuquerque, NM 87193
Please make changes accordingly, thank you for your attention in this matter.
Industry/Entity Type
Construction
Contact Information for Business Card
482 Montrose Ave NE, Albuquerque, NM 87193, Dorian Wexhall, Vice President, dorian@rvtfleetmotors.com, www.RVTfleetmotors.com, ph 505-271-6048, fax 505-617-2094, cell 505-438-7720

```html
<!DOCTYPE html>
<html lang="en">
<head>
<meta charset="utf-8">
<title>RVT Auto Sales – Business Card</title>
<link href="https://fonts.googleapis.com/css2?family=Arimo:wght@400;700&display=swap" rel="stylesheet">
<style>
  :root {
    --stage: #1e1e1e;
    --card-white: #ffffff;
    --card-textured: #f3f3f1;
    --ink: #151515;
    --accent: #e8232f;
    --accent-soft: #f07c7c;
    --icon: #ea6b6b;
  }
  * { box-sizing: border-box; margin: 0; padding: 0; }
  html, body {
    width: 1200px; height: 1000px; overflow: hidden;
    background: var(--stage);
    font-family: "Arimo", Arial, sans-serif;
    color: var(--ink);
  }
  .stage { position: relative; width: 1200px; height: 1000px; }
  .card {
    position: absolute;
    width: 805px; height: 460px;
    background: var(--card-white);
    box-shadow: 0 10px 30px rgba(0,0,0,.5);
  }
  .card--solid { left: 340px; top: 30px; }
  .card--outline { left: 55px; top: 510px; background: var(--card-textured); }

  .name-tab {
    position: absolute; right: 0; top: 52px;
    width: 330px; height: 84px;
    border-radius: 42px 0 0 42px;
    padding: 14px 28px 0 0;
    text-align: right;
  }
  .card--solid .name-tab { background: var(--accent-soft); }
  .card--outline .name-tab { border: 2px solid var(--ink); border-right: none; }
  .name-tab__name { font-weight: 700; font-size: 29px; line-height: 1.1; }
  .name-tab__title { font-size: 21px; line-height: 1.2; }

  .brand {
    position: absolute; left: 92px; top: 235px;
    display: flex; align-items: center; gap: 14px;
    font-weight: 700; font-size: 40px; line-height: 1;
    color: var(--ink);
  }
  .brand__mark { width: 20px; height: 20px; background: var(--ink); }

  .address {
    position: absolute; left: 92px; top: 318px;
    font-size: 27px; line-height: 1.25;
  }

  .contact {
    position: absolute; right: 40px; top: 205px;
    text-align: right;
  }
  .phones { list-style: none; }
  .phones li {
    display: flex; justify-content: flex-end; align-items: center;
    gap: 14px; font-size: 24px; line-height: 1.3;
  }
  .phones svg { width: 22px; height: 22px; }
  .online { margin-top: 22px; font-size: 22px; line-height: 1.25; }
  .online__web em { font-style: normal; color: var(--accent); }
</style>
</head>
<body>
<svg width="0" height="0" style="position:absolute" aria-hidden="true">
  <symbol id="icon-cell" viewBox="0 0 24 24">
    <circle cx="12" cy="12" r="12" fill="var(--icon)"/>
    <rect x="8.5" y="5" width="7" height="14" rx="1.2" fill="none" stroke="#222" stroke-width="1.4"/>
    <line x1="11" y1="16.5" x2="13" y2="16.5" stroke="#222" stroke-width="1.4"/>
  </symbol>
  <symbol id="icon-fax" viewBox="0 0 24 24">
    <circle cx="12" cy="12" r="12" fill="var(--icon)"/>
    <rect x="6" y="10" width="12" height="7" rx="1" fill="none" stroke="#222" stroke-width="1.4"/>
    <rect x="8.5" y="6" width="7" height="4" fill="none" stroke="#222" stroke-width="1.2"/>
  </symbol>
  <symbol id="icon-phone" viewBox="0 0 24 24">
    <circle cx="12" cy="12" r="12" fill="var(--icon)"/>
    <path d="M8 6c1 0 1.6 2.3 1.6 3s-1 1-1 1.6 2.3 3.5 3.3 3.8c.6 0 .8-1 1.5-1s3 .8 3 1.7-1 2.4-2.4 2.4C10 17.5 6.5 13 6.5 9 6.5 7 7.2 6 8 6z" fill="#222"/>
  </symbol>
</svg>

<main class="stage">
  <article class="card card--solid">
    <div class="name-tab">
      <p class="name-tab__name">Dorian Wexhall</p>
      <p class="name-tab__title">Vice President</p>
    </div>
    <p class="brand"><span class="brand__mark"></span>RVT Auto Sales</p>
    <p class="address">482 Montrose Ave NE<br>Albuquerque, NM 87193</p>
    <div class="contact">
      <ul class="phones">
        <li><svg><use href="#icon-cell"/></svg>505-438-7720</li>
        <li><svg><use href="#icon-fax"/></svg>505-271-6048</li>
        <li><svg><use href="#icon-phone"/></svg>505-617-2094</li>
      </ul>
      <div class="online">
        <p class="online__email">dorian@rvtfleetmotors.com</p>
        <p class="online__web">www.<em>RVTfleetmotors</em>.com</p>
      </div>
    </div>
  </article>

  <article class="card card--outline">
    <div class="name-tab">
      <p class="name-tab__name">Dorian Wexhall</p>
      <p class="name-tab__title">Vice President</p>
    </div>
    <p class="brand"><span class="brand__mark"></span>RVT Auto Sales</p>
    <p class="address">482 Montrose Ave NE<br>Albuquerque, NM 87193</p>
    <div class="contact">
      <ul class="phones">
        <li><svg><use href="#icon-cell"/></svg>505-438-7720</li>
        <li><svg><use href="#icon-fax"/></svg>505-271-6048</li>
        <li><svg><use href="#icon-phone"/></svg>505-617-2094</li>
      </ul>
      <div class="online">
        <p class="online__email">dorian@rvtfleetmotors.com</p>
        <p class="online__web">www.<em>RVTfleetmotors</em>.com</p>
      </div>
    </div>
  </article>
</main>
</body>
</html>
```